IT Company Business Card Rebranding

We want to modernize our business cards massively. We want to incorporate aspects of our old business card such as the white and geometric design with the blues of another icon. Existing Logo, old business card and icon are all attached.

We are a modern IT company that provides support for new and growing technologies and want our business cards to be modern yet professional.
Updates

Note: Do not use file ICON.png in design. This is just a design we like Added Wednesday, March 9, 2016

Industry/Entity Type

Information Technology

Contact Information for Business Card

Roughly 43 : 26 or 1075 x 650 px

Font styles to use
Serif

Colors
0492cd
3276b5
33a6d7
86cfc6
cfeae6
cee9f5
ffffff

Requirements
Must have
• Modern yet professional
Nice to have
• We would like to incorporate the blues of our existing logo and of the icon provided. Really like the design of the icon.
Should not have
• Too Decorative. Just simple and professional.
• Not have the circle icon, as it is a copyrighted icon, I just like the colors and the geometric design

```html
<!DOCTYPE html>
<html lang="en">
<head>
<meta charset="utf-8">
<title>Tech Ascend – Business Card</title>
<link rel="stylesheet" href="https://fonts.googleapis.com/css2?family=Tinos:wght@400;700&display=swap">
<style>
  :root {
    --page: #e8e9ee;
    --navy: #1b1c52;
    --ribbon: #1d8fcb;
    --ribbon-dark: #16709f;
    --sky-light: #d7f1f8;
    --sky-mid: #7fd0e8;
    --sky-deep: #33a6d7;
    --logo-grey: #5b6f86;
    --logo-blue: #3276b5;
    --icon-blue: #33a6d7;
    --white: #ffffff;
  }
  * { margin: 0; padding: 0; box-sizing: border-box; }
  html, body {
    width: 1200px; height: 970px; overflow: hidden;
    background: var(--page);
    font-family: "Tinos", "Times New Roman", serif;
  }
  .card {
    position: absolute; left: 100px; top: 182px;
    width: 1000px; height: 605px;
    background: var(--navy);
    box-shadow: 0 14px 34px rgba(20, 24, 60, 0.28);
    overflow: hidden;
  }
  .card__pattern {
    position: absolute; left: 0; top: 0;
    width: 570px; height: 100%;
    background:
      radial-gradient(ellipse at 30% 10%, rgba(255,255,255,0.85) 0%, rgba(255,255,255,0) 55%),
      linear-gradient(160deg, var(--sky-light) 0%, var(--sky-mid) 55%, var(--sky-deep) 100%);
  }
  .brand {
    position: absolute; left: 0; top: 345px; width: 570px;
    display: flex; align-items: center; justify-content: center; gap: 18px;
  }
  .brand__dot {
    width: 22px; height: 22px; border-radius: 50%;
    background: var(--logo-blue);
  }
  .brand__name {
    font-size: 44px; font-weight: 400; letter-spacing: 12px;
    color: var(--logo-grey); text-transform: uppercase;
  }
  .ribbon {
    position: absolute; left: 460px; top: 48px;
    width: 380px; height: 78px;
    background: var(--ribbon);
    box-shadow: 0 6px 10px rgba(0,0,0,0.25);
    color: var(--white);
    text-align: center;
    padding-top: 8px;
  }
  .ribbon::after {
    content: ""; position: absolute; left: 0; bottom: -10px;
    border-top: 10px solid var(--ribbon-dark);
    border-left: 12px solid transparent;
  }
  .ribbon__name { font-size: 36px; font-weight: 700; letter-spacing: 1px; line-height: 1.05; }
  .ribbon__role { font-size: 17px; letter-spacing: 0.5px; text-transform: uppercase; }
  .contacts {
    position: absolute; left: 650px; top: 212px;
    list-style: none; color: var(--white);
  }
  .contacts__item {
    display: flex; align-items: center; gap: 22px;
    height: 38px; font-size: 19px;
  }
  .contacts__item:first-child { font-size: 21px; letter-spacing: 0.5px; }
  .contacts__icon { width: 24px; height: 22px; fill: var(--icon-blue); flex: none; }
</style>
</head>
<body>
  <main class="card">
    <div class="card__pattern" role="img" aria-label="Light blue geometric triangle pattern background"></div>

    <div class="brand">
      <span class="brand__dot"></span>
      <span class="brand__name">Tech Ascend</span>
    </div>

    <div class="ribbon">
      <div class="ribbon__name">ETHAN</div>
      <div class="ribbon__role">Technical Service</div>
    </div>

    <ul class="contacts">
      <li class="contacts__item">
        <svg class="contacts__icon" viewBox="0 0 24 22" aria-hidden="true">
          <path d="M2 8c0-3 3-5 10-5s10 2 10 5v2h-5V7.5c-1.5-.7-8.5-.7-10 0V10H2z"/>
          <rect x="6" y="11" width="12" height="8" rx="2"/>
        </svg>
        <span>5550 987 654</span>
      </li>
      <li class="contacts__item">
        <svg class="contacts__icon" viewBox="0 0 24 22" aria-hidden="true">
          <path d="M2 4h20v14H2z M3.5 5.5l8.5 7 8.5-7" fill="none" stroke="#33a6d7" stroke-width="2"/>
        </svg>
        <span>info@mail.com</span>
      </li>
      <li class="contacts__item">
        <svg class="contacts__icon" viewBox="0 0 24 22" aria-hidden="true">
          <path d="M12 2L1 11h3v9h6v-6h4v6h6v-9h3z"/>
        </svg>
        <span>www.website.com</span>
      </li>
    </ul>
  </main>
</body>
</html>
```